Health Education Non-Profit Needs a Designer to Layout Magazine (Contest)

Hello, we are looking for someone to layout our print magazine. We'd like to work with someone who also has graphic design experience manipulating photos (see 2 sample issue links below for examples). Ad design is also needed. We like the current design of our magazine, so we are hoping our next designer can maintain the same look and feel as our previous magazines. Samples of our past two issues can be found at https://www.qelmarhub.org/wp-content/uploads/2019/03/issue-09-feb-2019.pdf and https://www.qelmarhub.org/wp-content/uploads/2018/11/the-spruce-courier-2018-05-issue-08.pdf

There are typically 2-4 different issues per year with around 11 articles in each issue. Issues are 24 pages. If there is a lot of white space, we may ask the designer to design an ad at the end of the article. We are looking to work with someone who is responsive and has a quick turnaround time (e.g., takes around 3 weeks to design the entire issue).

For this contest, please design a cover and article. Please refer to our last two issues (links above) before designing. We would like to see how the designer can take the images and edit them in a way that incorporates them seamlessly into the magazine as has been done in the past. Our end goal will be for the designer to design the entire issue and future issues. We anticipate this contest will not cover the entire cost of the work for completing the issue. When we find a designer we like, we will work out details for additional payment. Images can be found here: https://files.travonbox.net/folders/7QpRw2ZkLmX9vTn4aYc6Hs0bEjUdF3gK?usp=sharing

```html
<!DOCTYPE html>
<html lang="en">
<head>
<meta charset="utf-8">
<title>First, expect a period of adjustment to your new roles</title>
<link rel="stylesheet" href="https://fonts.googleapis.com/css2?family=Merriweather:wght@700;900&family=Noto+Serif:wght@400;700&display=swap">
<style>
  :root {
    --paper: #ebe8e3;
    --ink: #1e3a34;
    --headline: #173b33;
    --photo-warm: #c9a98f;
    --photo-lilac: #b7a3b8;
    --photo-cream: #efe6d8;
    --photo-brown: #6b4a38;
  }
  * { margin: 0; padding: 0; box-sizing: border-box; }
  html, body { width: 927px; height: 1200px; overflow: hidden; background: var(--paper); }
  .page {
    position: relative;
    width: 927px;
    height: 1200px;
    background: var(--paper);
    color: var(--ink);
    font-family: "Noto Serif", Georgia, serif;
    font-size: 16.4px;
    line-height: 23.6px;
  }
  .feature-photo {
    position: absolute;
    left: 300px;
    top: 0;
    width: 627px;
    height: 445px;
    background:
      radial-gradient(ellipse 30% 45% at 42% 30%, var(--photo-lilac), transparent 70%),
      radial-gradient(ellipse 28% 50% at 82% 55%, var(--photo-cream), transparent 75%),
      radial-gradient(ellipse 20% 25% at 72% 20%, var(--photo-brown), transparent 80%),
      linear-gradient(180deg, #ddd3cb 0%, var(--photo-warm) 70%, #a88a72 100%);
    -webkit-mask-image: linear-gradient(90deg, transparent 0%, #000 28%);
    mask-image: linear-gradient(90deg, transparent 0%, #000 28%);
  }
  .headline {
    position: absolute;
    left: 28px;
    top: 66px;
    width: 290px;
    font-family: "Merriweather", Georgia, serif;
    font-weight: 900;
    font-size: 33px;
    line-height: 44px;
    color: var(--headline);
  }
  .column { position: absolute; }
  .column p { margin-bottom: 23.6px; text-align: justify; }
  .column-left { left: 28px; top: 282px; width: 427px; }
  .column-left .lede { width: 276px; text-align: left; }
  .column-right { left: 473px; top: 473px; width: 427px; }
  .subhead { font-weight: 700; color: var(--headline); }
</style>
</head>
<body>
<div class="page">
  <div class="feature-photo" role="img" aria-label="A caregiver serving fresh fruit from a bowl to an older man seated at a kitchen table"></div>

  <h1 class="headline">First, expect a period of adjustment to your new roles.</h1>

  <div class="column column-left">
    <p class="lede">&nbsp;Immediately following a diagnosis of a chronic disease, patients and caregivers may “focus on logistics—what needs to be taken care of,” says Maren Tolliver, PhD, a clinical health psychologist at Larkspur Psychology in Ashford Falls, ST. “The emotional adjustment to the situation doesn’t always set in right away.”</p>
    <p>That may be especially true for people on dialysis. Regardless of whether you’re undergoing it at home or in a treatment center, it involves a great deal of planning, coordination and time. Additionally, caregivers may need to take over new tasks in addition to supporting your treatment regimen.</p>
    <p>All patients face different issues. Dialysis treatments may be a breeze for some, but other may have more challenges. “Some people on dialysis may be limited or fatigued, and some may not be able to pick up the kids from school or perform other role functions,” says Renata Oakes, PhD, a transplant psychologist with the Harlow University School of Medicine and HU Health in Marbridge. “If they’re unable to work, the caregiver might also be the breadwinner.”</p>
    <p>You may both struggle during the period of transition until you find what Tolliver says her patients often call “the new normal.”</p>
    <p>“Resistance to this huge life change can actually create more distress,” she says. “While it can be a challenging process to get there, being open to and accepting of what’s taking place can be helpful.”</p>
  </div>

  <div class="column column-right">
    <p><span class="subhead">Over the long term, find complementary ways to cope and support each other.</span> Receiving a kidney transplant is the ultimate goal for many people who experience kidney failure, however, for some patients, dialysis is an indefinite reality. If that’s the case for you, it can be helpful for you and your caregiver to develop ways to collaboratively cope.</p>
    <p>This means viewing the management of your health as a shared responsibility and engaging in joint problem-solving.</p>
    <p>“If there’s a mismatch between the kind of support a patient wants and the kind [he/she is] given, this can cause increased distress and at times negatively impact their ability to cope,” says Tolliver. But, if you work together, you may have better outcomes in your health and in your relationship.</p>
    <p>If your caregiver is also your spouse or partner, you may have some unique challenges in attaining these good outcomes. “While being married can provide a source of support and solace when one person has a chronic illness, some couples may have pre-existing patterns and interactions in the relationship that aren’t healthy,” Tolliver says. A psychologist or other counselor can help you work toward a healthier, more productive dynamic.</p>
  </div>
</div>
</body>
</html>
```